Web Design Project for Web Agency

WHAT I NEED:
The design I need (PSD file) is for a microsite designed for employee recruitment for Brantley, a Web agency.
***Design for the 1st Page ONLY : "Manifeste"
OBJECTIVES OF THE WEBSITE:
1. To promote the agency's corporate culture and HR management principles.
2. To get people to apply on available jobs
ELEMENTS OF THE PAGE "MANIFESTE" :
1. Brantley logo (see attached files). Beside the logo must be the word "Carrières" ("Careers" in english)
***The logo is not final and there is NO branding for Brantley yet. That is why there are multiple files. So please feel free to be creative!
2. Main menu : 4 sections
Manifeste | Opportunités | Brantly | Postuler
3. Manifeste :
This page is the home page. It will present 2 main sections :
a. The agency's corporate culture :
- Title of the page is a question : "Do you embrace Brantley's corporate culture?"
- Then, presentation of the 5 corporate values, each with a title and short description
- At the end of the list of values, we want a button that says "Apply now"
b. The agency's HR management principles :
- Title of the page is a question : "Do you see yourself working at Brantley?"
- Then, presentation of the 5 Management principles, each with a title and short description
- At the end of the list of principles, we want a button that says "Apply now"
VISUAL INSPIRATION
To create each section of the "Manifeste" page, we want a design that will fit with the corporate culture:
- Brantley is BOLD
- Brantley is PROUD
- Brantley is PROFESSIONAL
- Brantley is ELEGANT
- Brantley is REFINED
We want something slick and modern. Here are some Website's that we like that can be of inspiration:
- http://www.studio-vetrak.com/en/services
- http://quorvinpanels.com/

```html
<!DOCTYPE html>
<html lang="en">
<head>
<meta charset="utf-8">
<title>Brantley – Careers</title>
<link rel="stylesheet" href="https://fonts.googleapis.com/css2?family=Arimo:ital,wght@0,400;0,700;1,400;1,700&family=Fredoka:wght@500&display=swap">
<style>
  :root {
    --orange: #f47a2c;
    --orange-deep: #f39325;
    --ink: #111111;
    --grey-text: #555555;
    --muted: #8a8a8a;
    --panel-light: #5a5a5a;
    --panel-dark: #1d1d1d;
    --white: #ffffff;
    --divider: #c9c9c9;
  }
  * { box-sizing: border-box; margin: 0; padding: 0; }
  html, body { width: 981px; height: 1200px; overflow: hidden; background: var(--white); }
  body { position: relative; font-family: "Arimo", Arial, sans-serif; color: var(--ink); }
  .abs { position: absolute; }

  .top-band { left: 0; top: 0; }
  .language { left: 87px; top: 24px; font-size: 12px; color: var(--muted); }
  .follow { left: 734px; top: 41px; font-size: 15px; color: #e8e8e8; }
  .social { top: 24px; width: 32px; height: 32px; border-radius: 6px; background: linear-gradient(#e6e6e6, #a9a9a9); border: 1px solid #888; }
  .social--one { left: 810px; }
  .social--two { left: 851px; }

  .brand { left: 90px; top: 92px; font-family: "Fredoka", "Arimo", sans-serif; font-weight: 500; font-size: 48px; color: var(--orange); letter-spacing: 1px; }

  .main-nav a { position: absolute; top: 164px; font-size: 16px; line-height: 18px; color: var(--ink); text-decoration: none; }
  .nav-divider { position: absolute; top: 162px; width: 1px; height: 30px; background: var(--divider); }

  .hero { left: 48px; top: 202px; width: 882px; height: 401px;
    background: radial-gradient(ellipse at 60% 40%, #f3e39c 0%, #d9c47a 30%, #9c9b7f 60%, #3f5264 100%); overflow: hidden; }
  .hero-title { left: 85px; top: 50px; font-size: 76px; font-weight: 700; font-style: italic; letter-spacing: 2px;
    color: #b58a4a; text-shadow: 3px 5px 6px rgba(0,0,0,.35); }
  .hero-arrow { top: 352px; width: 42px; height: 42px; border-radius: 50%; border: 2px solid var(--white); background: #3b362c; }
  .hero-arrow--prev { left: 57px; } .hero-arrow--next { left: 111px; }
  .hero-arrow svg { display: block; margin: 12px auto; }

  .hero-rule { left: 48px; top: 603px; width: 882px; height: 11px; background: linear-gradient(90deg, var(--orange-deep) 0%, var(--orange) 40%, #fbe0c2 75%, #f3f3f3 100%); }

  .values-panel { left: 48px; top: 614px; width: 882px; height: 266px; background: linear-gradient(90deg, var(--panel-light), #3a3a3a 60%, var(--panel-dark)); color: var(--white); }
  .pillar { top: 30px; }
  .pillar--culture { left: 53px; } .pillar--hr { left: 452px; }
  .pillar h2 { font-size: 19px; font-weight: 700; }
  .pillar p { margin-top: 10px; font-size: 16.5px; font-style: italic; }
  .read-more { top: 107px; font-size: 16px; font-weight: 700; font-style: italic; color: var(--orange); text-decoration: none; }
  .read-more--culture { left: 288px; } .read-more--hr { left: 697px; }
  .apply { left: 307px; top: 186px; width: 170px; height: 51px; border-radius: 8px; background: linear-gradient(#f2f2f2, #8d8d8d); border: none;
    font-family: inherit; font-size: 23px; font-weight: 700; font-style: italic; color: var(--ink); padding-left: 6px; }

  .footer-bg { left: 48px; top: 905px; }
  .footer-col { top: 1013px; }
  .footer-col h3 { font-size: 18px; font-weight: 400; margin-bottom: 6px; }
  .footer-col li { list-style: none; font-size: 13px; line-height: 16.5px; color: var(--grey-text); }
  .footer-contact { left: 120px; } .footer-contact li { padding-left: 2px; }
  .footer-menu { left: 383px; }
  .footer-menu li.strong { color: var(--ink); }
  .footer-menu li.tight { line-height: 13px; margin-bottom: 3px; }
  .footer-news { left: 568px; width: 290px; }
  .footer-news p { font-size: 13px; line-height: 16px; color: var(--grey-text); }
  .footer-news label { display: block; margin-top: 17px; font-size: 18px; }
  .email-field { margin-top: 8px; width: 240px; height: 32px; border-radius: 16px; border: 2px solid var(--ink); background: linear-gradient(90deg, #444, #777); position: relative; }
  .email-field input { position: absolute; left: 46px; top: 0; width: 190px; height: 28px; border-radius: 14px; border: none; background: var(--white); }
</style>
</head>
<body>
  <svg class="abs top-band" width="981" height="135" viewBox="0 0 981 135" aria-hidden="true">
    <defs>
      <linearGradient id="bandDark" x1="0" x2="1"><stop offset="0" stop-color="#7a7a7a"/><stop offset="0.5" stop-color="#333"/><stop offset="1" stop-color="#1b1b1b"/></linearGradient>
      <linearGradient id="bandOrange" x1="0" x2="1"><stop offset="0" stop-color="#fde6cc"/><stop offset="1" stop-color="#f39325"/></linearGradient>
    </defs>
    <polygon points="437,0 931,0 931,130" fill="url(#bandOrange)"/>
    <polygon points="452,0 931,0 931,117" fill="url(#bandDark)"/>
  </svg>

  <div class="abs language">Select: Language</div>
  <div class="abs follow">Follow us:</div>
  <span class="abs social social--one" aria-label="Social network"></span>
  <span class="abs social social--two" aria-label="Social network"></span>

  <div class="abs brand">Brantley</div>

  <nav class="main-nav">
    <a href="#" style="left:356px;top:166px">Home</a>
    <span class="nav-divider" style="left:419px"></span>
    <a href="#" style="left:438px;top:166px">About</a>
    <span class="nav-divider" style="left:500px"></span>
    <a href="#" style="left:515px">Manifeste</a>
    <span class="nav-divider" style="left:594px"></span>
    <a href="#" style="left:604px">Opportunités</a>
    <span class="nav-divider" style="left:705px"></span>
    <a href="#" style="left:716px">Brantly</a>
    <span class="nav-divider" style="left:781px"></span>
    <a href="#" style="left:791px">Postuler</a>
  </nav>

  <section class="abs hero" role="img" aria-label="Photo of a person standing triumphant on a cliff edge against a golden sunset sky">
    <div class="abs hero-title">CAREER...</div>
    <span class="abs hero-arrow hero-arrow--prev"><svg width="14" height="14" viewBox="0 0 14 14"><polygon points="11,1 11,13 2,7" fill="#fff"/></svg></span>
    <span class="abs hero-arrow hero-arrow--next"><svg width="14" height="14" viewBox="0 0 14 14"><polygon points="3,1 3,13 12,7" fill="#fff"/></svg></span>
  </section>
  <div class="abs hero-rule"></div>

  <section class="abs values-panel">
    <div class="abs pillar pillar--culture">
      <h2>The agency's corporate culture</h2>
      <p>"Do you embrace Brantley's corporate culture?"</p>
    </div>
    <div class="abs pillar pillar--hr">
      <h2>The agency's HR management principles :</h2>
      <p>"Do you see yourself working at Brantley?"</p>
    </div>
    <a class="abs read-more read-more--culture" href="#">Read more&gt;&gt;</a>
    <a class="abs read-more read-more--hr" href="#">Read more&gt;&gt;</a>
    <button class="abs apply">Apply now</button>
  </section>

  <svg class="abs footer-bg" width="882" height="295" viewBox="0 0 882 295" aria-hidden="true">
    <defs>
      <linearGradient id="footerFill" x1="0" y1="0" x2="1" y2="0.4">
        <stop offset="0" stop-color="#fffaf3"/><stop offset="0.5" stop-color="#fdf0dc"/>
        <stop offset="0.8" stop-color="#fbc583"/><stop offset="1" stop-color="#f6931f"/>
      </linearGradient>
    </defs>
    <polygon points="0,5 882,105 882,295 0,295" fill="url(#footerFill)"/>
  </svg>

  <div class="abs footer-col footer-contact">
    <h3>Contact</h3>
    <ul>
      <li>xxxxxxx</li>
      <li>xxxxxxxxxxxxxxxxxxxxxx</li>
      <li>xxxxxxxxxxxxxx</li>
      <li>xxxxxxxxxxxxx</li>
      <li>xxxxxxxx</li>
    </ul>
  </div>
  <div class="abs footer-col footer-menu">
    <h3>Menu</h3>
    <ul>
      <li class="strong tight">Home</li>
      <li class="strong tight">About</li>
      <li>Manifeste</li>
      <li>Opportunités</li>
      <li>Brantly</li>
      <li>Postuler</li>
    </ul>
  </div>
  <div class="abs footer-col footer-news">
    <h3>Newsletter</h3>
    <p>Exciting carrer opportunities &amp; more through newsletter</p>
    <label for="email">Enter Your Email Address</label>
    <div class="email-field"><input id="email" type="email" aria-label="Email address"></div>
  </div>
</body>
</html>
```